Convert this PSD to vector, first one wins

I am having a hell of a time figuring out how to do this, and I have too much going on right now. I need help.

Needs to be Illustrator EPS. It is all white lettering accept for the top logo. No background.

```html
<!DOCTYPE html>
<html lang="en">
<head>
<meta charset="utf-8">
<title>The Lark Residence – Sales Center</title>
<link rel="stylesheet" href="https://fonts.googleapis.com/css2?family=Cabin:wght@400;500;600&display=swap">
<style>
  :root {
    --clay: #9a5f3b;
    --stone: #a3a292;
    --stone-dark: #6b4a2a;
    --ink: #ffffff;
    --font: "Cabin", sans-serif;
  }
  html, body {
    margin: 0;
    padding: 0;
    width: 1200px;
    height: 2880px;
    overflow: hidden;
    background: var(--clay);
  }
  .banner {
    position: relative;
    width: 1200px;
    height: 2880px;
    background: var(--clay);
    color: var(--ink);
    font-family: var(--font);
    text-align: center;
  }
  .line {
    position: absolute;
    left: 0;
    width: 1200px;
    margin: 0;
    white-space: nowrap;
    text-transform: uppercase;
  }
  .brand-band {
    position: absolute;
    top: 0;
    left: 0;
    width: 1200px;
    height: 176px;
    background: var(--stone);
    display: flex;
    align-items: center;
    justify-content: center;
    gap: 36px;
  }
  .brand-mark {
    width: 46px;
    height: 46px;
    background: var(--stone-dark);
  }
  .brand-name {
    font-size: 74px;
    font-weight: 400;
    letter-spacing: 10px;
    color: var(--ink);
    margin: 0;
  }
  .center-title { top: 370px; font-size: 96px; font-weight: 600; letter-spacing: 16px; line-height: 96px; }
  .center-address { top: 500px; font-size: 66px; font-weight: 500; letter-spacing: 3px; line-height: 66px; }
  .rule {
    position: absolute;
    left: 246px;
    width: 708px;
    height: 3px;
    background: var(--ink);
  }
  .rule-top { top: 741px; }
  .rule-bottom { top: 1311px; }
  .day { font-size: 66px; font-weight: 600; letter-spacing: 14px; line-height: 66px; }
  .hours { font-size: 58px; font-weight: 400; letter-spacing: 6px; line-height: 58px; }
  .weekdays { top: 803px; }
  .weekdays-hours { top: 899px; }
  .sunday { top: 1096px; }
  .sunday-hours { top: 1194px; }
  .appointment { top: 1474px; font-size: 66px; font-weight: 600; letter-spacing: 14px; line-height: 66px; }
  .phone { top: 1587px; font-size: 60px; font-weight: 400; letter-spacing: 10px; line-height: 60px; }
  .agency {
    position: absolute;
    left: 0;
    top: 2400px;
    width: 1200px;
    display: flex;
    flex-direction: column;
    align-items: center;
    gap: 30px;
    font-weight: 600;
    text-transform: uppercase;
  }
  .agency-name { font-size: 120px; letter-spacing: 4px; line-height: 120px; }
  .agency-sub { font-size: 62px; letter-spacing: 6px; line-height: 62px; }
  .website { top: 2818px; font-size: 64px; font-weight: 400; letter-spacing: 14px; line-height: 64px; }
</style>
</head>
<body>
  <main class="banner">
    <header class="brand-band">
      <span class="brand-mark"></span>
      <h1 class="brand-name">THE LARK RESIDENCE</h1>
    </header>

    <h2 class="line center-title">Sales Center</h2>
    <p class="line center-address">240 North Pine Street</p>

    <div class="rule rule-top"></div>

    <p class="line day weekdays">Weekdays</p>
    <p class="line hours weekdays-hours">11:00 AM - 6:00 PM</p>
    <p class="line day sunday">Sunday</p>
    <p class="line hours sunday-hours">1:00 PM - 3:00 PM</p>

    <div class="rule rule-bottom"></div>

    <p class="line appointment">By Appointment</p>
    <p class="line phone">(555) 014-2300</p>

    <div class="agency">
      <span class="agency-name">Keystone</span>
      <span class="agency-sub">Realty Group</span>
    </div>

    <p class="line website">larkresidence.org</p>
  </main>
</body>
</html>
```